Strategy and Technology Consulting - Our Story and Values Page

Interior Page design – Our History and Our Values

Our homepage has been designed and we are looking for a design for one of the interior pages. This interior page tells the story of Our History and Our Values

Because the homepage has been designed, we would like this interior page to reflect the design of the homepage without being a mirror image of the homepage.

This site will be implemented in WordPress using the Elementor framework.

Font: Poppins medium and Poppins dark
Illustrations: Our homepage illustrations were designed by “Welmo 1974” on Pixaborne. Compatible original or stock illustrations are welcome. Stock photography is also welcome. Welmo is also available through Welmo Trastek on Folivane

Uploaded Files
• Homepage design – this is the design we will use for our homepage. Contest entries should reflect this basic style but should be distinctly different from the homepage.
• Our History and Our Values – Wireframe – the basic layout of the page we are looking for.
• Our History and Our Values – Word document with the text supporting the wireframe.
• Color Palette – please use colors compatible with the palette attached.

Our Story - timeline
There is a timeline element in the wireframe. The wireframe displays this as a series of chevrons (arrows), but it does not need to be. Creativity in display of the timeline is appreciated.

Our Values
If you look at the Word document, you will see that there are a lot of words on the page. The winning design will present the information in a way that engages the user without overwhelming them with too much to read. For example, they may click on a value and see more information.

Target Market(s)

CIO's and Technology Executives

Number of Pages Required

1 page

Font styles to use
Sans Serif
Other font styles liked:
• Poppin

Requirements
Must have
• A timeline element, all of our values
Nice to have
• Clever timeline display

```html
<!DOCTYPE html>
<html lang="en">
<head>
<meta charset="UTF-8">
<title>Our History &amp; Our Values</title>
<link href="https://fonts.googleapis.com/css2?family=Poppins:wght@400;500;600;700&display=swap" rel="stylesheet">
<style>
:root{
  --blue:#2f6fc2;
  --blue-light:#a9cdef;
  --orange:#f39a1c;
  --yellow:#f8c52b;
  --yellow-dark:#e9a91a;
  --ink:#1d2433;
  --muted:#5b6270;
  --white:#ffffff;
  --card-line:#e6e8ec;
}
*{margin:0;padding:0;box-sizing:border-box}
html,body{width:669px;height:1200px;overflow:hidden;background:var(--white);font-family:"Poppins",sans-serif;color:var(--ink)}
.page{position:relative;width:669px;height:1200px}
.history{position:absolute;top:0;left:0;width:669px;height:300px}
.history-bg{position:absolute;top:0;left:0}
.section-title{position:absolute;font-weight:700;font-size:19px;color:var(--orange)}
.history .section-title{top:28px;left:46px}
.timeline{position:absolute;top:76px;left:30px;width:610px;height:22px}
.phase-label{position:absolute;top:0;height:22px;line-height:22px;font-size:9.5px;font-weight:600;color:var(--white);text-align:center}
.phase-list{position:absolute;top:120px;list-style:none;font-size:8.5px;line-height:13.5px;color:var(--white)}
.phase-list li{position:relative;padding-left:11px}
.phase-list li::before{content:"";position:absolute;left:0;top:5px;width:4px;height:4px;border-radius:50%;background:var(--yellow)}
.phase-list li.sub{padding-left:19px}
.phase-list li.sub::before{display:none}
.values .section-title{top:310px;left:46px}
.card{position:absolute;width:147px;height:260px;background:var(--white);border:1px solid var(--card-line);box-shadow:0 2px 8px rgba(0,0,0,.08);padding:8px 10px;text-align:center}
.card-art{height:100px;margin:0 0 8px;border-radius:4px;background:linear-gradient(160deg,#dbe8f8,#f4d9a6)}
.card h3{font-size:10px;font-weight:700;line-height:12px;margin-bottom:5px}
.card p{font-size:5.8px;line-height:8.4px;color:var(--muted)}
</style>
</head>
<body>
<div class="page">
  <section class="history">
    <svg class="history-bg" width="669" height="300" viewBox="0 0 669 300">
      <path d="M0 0H669V270C600 300 540 245 460 260C380 275 330 240 250 252C170 264 90 235 0 262Z" fill="var(--blue-light)"/>
      <path d="M0 0H669V235C590 262 520 210 440 228C360 246 300 205 220 222C140 239 70 205 0 230Z" fill="var(--blue)"/>
    </svg>
    <h2 class="section-title">Our History</h2>
    <div class="timeline">
      <svg width="610" height="22" viewBox="0 0 610 22">
        <path d="M0 0H198L208 11L198 22H0L8 11Z" fill="var(--yellow)"/>
        <path d="M204 0H400L410 11L400 22H204L214 11Z" fill="var(--yellow)"/>
        <path d="M406 0H600L610 11L600 22H406L416 11Z" fill="var(--yellow)"/>
      </svg>
      <span class="phase-label" style="left:0;width:205px">2017 – 2019</span>
      <span class="phase-label" style="left:207px;width:200px">2020 – 2021</span>
      <span class="phase-label" style="left:409px;width:200px">2022 &amp; Onward</span>
    </div>
    <ul class="phase-list" style="left:46px">
      <li>Growth Strategy Focus</li>
      <li>Consistent, Modest Growth</li>
      <li>Preliminary Focus On Technology</li>
      <li>Context Implementing Strategy<br>is Hard</li>
    </ul>
    <ul class="phase-list" style="left:250px">
      <li>Pandemic Pauses Growth</li>
      <li>Rethinking:</li>
      <li class="sub">– The business model</li>
      <li class="sub">– The delivery model</li>
    </ul>
    <ul class="phase-list" style="left:452px">
      <li>Leadership Team for Focus<br>on Essential Areas</li>
      <li>Rapid Growth</li>
      <li>Customer Success</li>
    </ul>
  </section>

  <section class="values">
    <h2 class="section-title">Our Values</h2>

    <article class="card" style="left:88px;top:346px">
      <div class="card-art" role="img" aria-label="Illustration of a diverse group of people standing together"></div>
      <h3>The Value of Every Human. Regardless.</h3>
      <p>Each person's unique experiences and perspectives add vibrant hues to the tapestry of our shared existence. In a world where diversity paints the canvas of humanity, true beauty is found in recognizing the inherent and incalculable value of every human being.</p>
    </article>

    <article class="card" style="left:261px;top:346px">
      <div class="card-art" role="img" aria-label="Illustration of a person reaching a target with an arrow"></div>
      <h3>Passion</h3>
      <p>Passion infuses our work with energy, transforming routine tasks into opportunities for creativity and innovation. Fueled by passion, individuals become unstoppable forces, driven to overcome challenges and achieve remarkable outcomes that benefit them and inspire those around them.</p>
    </article>

    <article class="card" style="left:435px;top:346px">
      <div class="card-art" role="img" aria-label="Illustration of a person on a summit holding a flag"></div>
      <h3>Excellence</h3>
      <p>Excellence isn't a destination; it's a continuous journey of refinement and growth. Striving for excellence cultivates a culture of continuous improvement, fostering innovation, credibility, and a lasting impact that resonates far beyond the immediate task.</p>
    </article>

    <article class="card" style="left:88px;top:628px">
      <div class="card-art" role="img" aria-label="Illustration of a person climbing upward steps"></div>
      <h3>Tenacity</h3>
      <p>Tenacity is the unwavering anchor that keeps us grounded amidst adversity, propelling us forward when faced with obstacles. The resilience to persist, adapt, and learn from setbacks leads to the mastery of skills and the fulfillment of ambitious goals.</p>
    </article>

    <article class="card" style="left:261px;top:628px">
      <div class="card-art" role="img" aria-label="Illustration of people assembling a large puzzle"></div>
      <h3>Solution Mindset</h3>
      <p>A solution mindset is the compass that directs our focus from problems to possibilities. It empowers us to navigate challenges with a proactive mindset, igniting a journey of exploration and innovation that not only resolves issues but discovers the way for continuous growth and success.</p>
    </article>

    <article class="card" style="left:435px;top:628px">
      <div class="card-art" role="img" aria-label="Illustration of a person offering a heart to another"></div>
      <h3>Generosity</h3>
      <p>Generosity creates a virtuous cycle of goodwill, fostering a sense of unity and shared purpose among colleagues. By freely sharing knowledge, support, and resources, we uplift those around us and contribute to a collaborative environment where collective achievements flourish.</p>
    </article>

    <article class="card" style="left:88px;top:910px">
      <div class="card-art" role="img" aria-label="Illustration of a team working together around a table"></div>
      <h3>Collaboration</h3>
      <p>Collaboration in work transforms individual endeavors into symphonies of collective achievement. Through collaboration, diverse talents converge, fostering a rich exchange of ideas that amplifies creativity, accelerates progress, and brings forth solutions beyond what a single mind could conceive.</p>
    </article>
  </section>
</div>
</body>
</html>
```